Looking to design a new sign for our church.

Looking for a new sign
4 x 8 feet dimension
We are renaming the church "Medlow Ridge Community Church"
looking for legible graphics
Would like some type of backdrop being a family tree (oak) / open to other ideas as you are led
I have included a pic of the old sign for your review
would like to incorporate our ministry logo on the lower right hand corner of the sign / see file attached

```html
<!DOCTYPE html>
<html lang="en">
<head>
<meta charset="utf-8">
<title>Medlow Ridge Community Church — Roadside Sign</title>
<link rel="stylesheet" href="https://fonts.googleapis.com/css2?family=Abril+Fatface&family=Playfair+Display:ital,wght@1,900&family=Montserrat:wght@400&display=swap">
<style>
  :root {
    --page: #e8e8e6;
    --sign: #f3efe4;
    --ink: #0b0b0b;
    --row-fill: #f7f5f0;
    --art-light: #efeadd;
    --art-dark: #1a1a1a;
  }
  * { margin: 0; padding: 0; box-sizing: border-box; }
  html, body {
    width: 1200px;
    height: 838px;
    overflow: hidden;
    background: var(--page);
  }
  .sign {
    position: absolute;
    left: 80px;
    top: 103px;
    width: 1040px;
    height: 631px;
    background: var(--sign);
    color: var(--ink);
    box-shadow: 0 0 0 22px #ffffff;
  }
  .ministry-mark {
    position: absolute;
    left: 52px;
    top: 230px;
    display: flex;
    flex-direction: column;
    align-items: center;
    gap: 8px;
    width: 104px;
  }
  .ministry-mark__dot {
    width: 58px;
    height: 58px;
    border-radius: 50%;
    background: var(--ink);
  }
  .ministry-mark__name {
    font-family: "Montserrat", sans-serif;
    font-size: 13px;
    text-align: center;
    line-height: 1.1;
  }
  .church-name {
    position: absolute;
    left: 168px;
    top: 28px;
    font-family: "Abril Fatface", serif;
    font-size: 120px;
    line-height: 108px;
    letter-spacing: 1px;
  }
  .church-name__rule {
    position: absolute;
    left: 171px;
    top: 283px;
    width: 272px;
    height: 2px;
    background: var(--ink);
  }
  .church-name__sub {
    position: absolute;
    left: 171px;
    top: 300px;
    font-family: "Playfair Display", serif;
    font-style: italic;
    font-weight: 900;
    font-size: 38px;
    letter-spacing: 4px;
  }
  .schedule {
    position: absolute;
    left: 59px;
    top: 409px;
    width: 518px;
    list-style: none;
  }
  .schedule__row {
    display: flex;
    height: 38px;
    margin-bottom: 21px;
    border: 1.5px solid var(--ink);
    background: var(--row-fill);
    font-family: "Montserrat", sans-serif;
    font-size: 30px;
    line-height: 35px;
  }
  .schedule__time {
    width: 149px;
    background: var(--ink);
    color: var(--sign);
    padding-left: 4px;
  }
  .schedule__event {
    padding-left: 16px;
  }
  .backdrop {
    position: absolute;
    left: 745px;
    top: 21px;
    width: 264px;
    height: 578px;
    border: 2px solid var(--ink);
    background: linear-gradient(180deg, var(--art-light) 0%, var(--art-light) 22%, #3a3a3a 48%, var(--art-dark) 100%);
  }
</style>
</head>
<body>
  <main class="sign">
    <div class="ministry-mark">
      <span class="ministry-mark__dot"></span>
      <span class="ministry-mark__name">Medlow Ridge</span>
    </div>

    <h1 class="church-name">Medlow<br>Ridge</h1>
    <div class="church-name__rule"></div>
    <p class="church-name__sub">Community Church</p>

    <ul class="schedule">
      <li class="schedule__row"><span class="schedule__time">10:30am</span><span class="schedule__event">Worship Service</span></li>
      <li class="schedule__row"><span class="schedule__time">9:30am</span><span class="schedule__event">Sunday School</span></li>
      <li class="schedule__row"><span class="schedule__time">6:00pm</span><span class="schedule__event">Wednesday Service</span></li>
    </ul>

    <div class="backdrop" role="img" aria-label="Black silhouette of a spreading oak tree in front of a rising sun with radiating lines, inside a tall frame"></div>
  </main>
</body>
</html>
```